Logo & Visitenkarte für ein Ingenieurbüro
Zielgruppe
Ich bin freiberuflich als Ingenieurbüro unterwegs. Projekte, Planungen erneuerbare Energien, Verbrauchsanalysen, Beratungen. Keine spezielle Zielgruppe. Grundthemen: Technik, Menschen, Netzwerk Verbinden
Aufgabenstellung
Das Design soll klar, vertrauensvoll, wertig, sysmpatisch sein.
Grundthemen: Technik, Menschen, Netzwerk, Verbinden
Rückseite: QR-Code von mir kommt dann nach Beratung

```html
<!DOCTYPE html>
<html lang="de">
<head>
<meta charset="utf-8">
<title>Falkenried – Visitenkarte</title>
<link rel="stylesheet" href="https://fonts.googleapis.com/css2?family=Poppins:wght@400;500;600;700&display=swap">
<style>
  :root {
    --backdrop: #262626;
    --card-dark: #323232;
    --card-light: #ffffff;
    --ink: #2b2b2b;
    --white: #ffffff;
    --accent: #8cc610;
  }
  * { margin: 0; padding: 0; box-sizing: border-box; }
  html, body {
    width: 1200px; height: 800px; overflow: hidden;
    background: var(--backdrop);
    font-family: "Poppins", sans-serif;
  }
  .canvas { position: relative; width: 1200px; height: 800px; }

  .card { position: absolute; width: 353px; height: 228px; }
  .card--front { left: 216px; top: 270px; background: var(--card-dark); color: var(--white); }
  .card--back { left: 632px; top: 269px; background: var(--card-light); color: var(--ink); }

  .wordmark { font-weight: 600; line-height: 1; white-space: nowrap; }

  .front-brand { position: absolute; left: 0; right: 0; top: 360px; text-align: center; }
  .card--front .wordmark {
    position: absolute; left: 0; right: 0; top: 89px;
    text-align: center; font-size: 28px; letter-spacing: 1.5px;
  }
  .card--front .tagline {
    position: absolute; left: 0; right: 0; top: 120px;
    text-align: center; font-size: 9.5px; font-weight: 500; letter-spacing: 2px;
  }
  .card--front .services {
    position: absolute; left: 0; right: 0; top: 193px;
    text-align: center; font-size: 8.5px; font-weight: 500; letter-spacing: 1.6px;
  }

  .card--back .wordmark {
    position: absolute; left: 28px; top: 19px;
    font-size: 22px; letter-spacing: 1px; color: var(--ink);
  }
  .card--back .office {
    position: absolute; left: 29px; top: 39px;
    font-size: 7px; font-weight: 500; letter-spacing: 5.3px;
  }
  .contact { position: absolute; left: 186px; top: 58px; }
  .contact__name { font-size: 13px; font-weight: 700; line-height: 1.2; }
  .contact__title { font-size: 10.5px; margin-top: 3px; }
  .contact__group { position: relative; margin-top: 12px; padding-left: 16px; font-size: 10.5px; line-height: 12.5px; }
  .contact__line { position: relative; display: block; white-space: nowrap; }
  .icon { position: absolute; left: -16px; top: 2px; width: 9px; height: 9px; fill: var(--accent); }
  .icon--mid { top: 7px; }

  .showcase-logo { position: absolute; left: 0; right: 0; top: 694px; text-align: center; color: var(--white); }
  .showcase-logo .wordmark { font-size: 40px; letter-spacing: 2.5px; }
  .showcase-logo .tagline { margin-top: 5px; font-size: 13px; font-weight: 500; letter-spacing: 2.8px; }
</style>
</head>
<body>
<main class="canvas">

  <section class="card card--front" aria-label="Vorderseite">
    <div class="wordmark">FALKENRIED</div>
    <div class="tagline">ENGINEERING NETWORKS</div>
    <div class="services">BERATUNG . PLANUNG . PROJEKTE</div>
  </section>

  <section class="card card--back" aria-label="Rückseite">
    <div class="wordmark">FALKENRIED</div>
    <div class="office">INGENIEURBÜRO</div>

    <div class="contact">
      <div class="contact__name">JONAS FALKENRIED</div>
      <div class="contact__title">Dipl. Ing. E-Technik</div>

      <div class="contact__group">
        <svg class="icon icon--mid" viewBox="0 0 10 10"><path d="M5 0a3.6 3.6 0 0 1 3.6 3.6C8.6 6.3 5 10 5 10S1.4 6.3 1.4 3.6A3.6 3.6 0 0 1 5 0zm0 2.2a1.4 1.4 0 1 0 0 2.8 1.4 1.4 0 0 0 0-2.8z"/></svg>
        <span class="contact__line">Lindenweg 14</span>
        <span class="contact__line">58000 Musterstadt</span>
      </div>

      <div class="contact__group">
        <span class="contact__line">
          <svg class="icon" viewBox="0 0 10 10"><path d="M2.2 0.4l1.6 2.1-.9 1.2c.6 1.3 1.6 2.3 2.9 2.9l1.2-.9 2.1 1.6-.8 1.8C5 9.3.7 5 .4 1.2z"/></svg>
          02000 - 12 34 560
        </span>
        <span class="contact__line">
          <svg class="icon" viewBox="0 0 10 10"><path d="M2.5 0h5v10h-5zM3.5 1v7h3V1z"/></svg>
          0170 - 00 11 220
        </span>
      </div>

      <div class="contact__group">
        <span class="contact__line">
          <svg class="icon" viewBox="0 0 10 10"><path d="M0 1.5h10v7H0zM1 2.5L5 5.5 9 2.5z" fill-rule="evenodd"/></svg>
          kontakt@j-falkenried.de
        </span>
        <span class="contact__line">
          <svg class="icon" viewBox="0 0 10 10"><circle cx="5" cy="5" r="4.3" fill="none" stroke="#8cc610" stroke-width="1.1"/><path d="M5 0.7v8.6M0.7 5h8.6" stroke="#8cc610" stroke-width="0.9"/><ellipse cx="5" cy="5" rx="2" ry="4.3" fill="none" stroke="#8cc610" stroke-width="0.9"/></svg>
          www.j-falkenried.de
        </span>
      </div>
    </div>
  </section>

  <div class="showcase-logo">
    <div class="wordmark">FALKENRIED</div>
    <div class="tagline">ENGINEERING NETWORKS</div>
  </div>

</main>
</body>
</html>
```